Design cover for information booklet
I am looking for a design for the front and back cover of an information booklet. Also an inside page basic design.
The booklet will contain 10 double sided pages providing information on weight loss surgery.
See my website www.brevinmarsh.com.au for what I do and typical colour themes.
I would also like some theming/illustration which can be utilised on each inside page of the booklet, rather than the pages just being blank with text etc. What would a blank page on this inside of the booklet look like under the design theme that you have created?
My company is Kestrel Institute for Metabolic Surgery. You will find uploaded a Logo for Kestrel Institute for Metabolic Surgery as well as my other logo which is my name “Brevin Marsh, etc.”. The Kestrel Institute for Metabolic Surgery logo should be utilised. The other logo (Brevin Marsh) is optional.
The front cover should contain the following text as minimum:
Kestrel Institute for Metabolic Surgery
Mr Brevin Marsh MBBS FRACS GradCert (Health Stats)
Our tagline is “Experience, Expertise and Empathy”. This should probably be on the front cover also.
The back cover contains (as a minimum) our address, phone number, fax number:
Suite 17, Level 3
Tallowgate Northern Hospital
9 Pemberly Road, Fernwick VIC 3174
Phone: 03 9412 6083
Fax: 03 9417 2865
Email: info@kestrelims.com.au
The files should be in a form whereby the text can be edited and changed if need be.
1. problems with initial graphical attachments - Artforge end 2. several requests by designers for extension

```html
<!DOCTYPE html>
<html lang="en">
<head>
<meta charset="utf-8">
<title>Kestrel Institute for Metabolic Surgery – Booklet Covers</title>
<link rel="stylesheet" href="https://fonts.googleapis.com/css2?family=Josefin+Sans:wght@400;600;700&family=EB+Garamond:ital,wght@0,400;0,600;1,400&display=swap">
<style>
  :root {
    --backdrop: #aca6a4;
    --teal: #5cbab2;
    --teal-deep: #16978b;
    --teal-line: #2aa79b;
    --paper: #f4f5f5;
    --paper-shade: #e4e6e7;
    --white: #ffffff;
    --lilac-edge: #c9c6e4;
  }
  * { box-sizing: border-box; margin: 0; padding: 0; }
  html, body { width: 1200px; height: 789px; overflow: hidden; }
  body {
    background: var(--backdrop);
    display: flex; align-items: center; justify-content: center;
  }
  .spread {
    width: 960px; height: 680px;
    display: flex;
    box-shadow: 0 10px 30px rgba(0,0,0,.25);
  }
  .cover {
    position: relative;
    width: 480px; height: 680px;
    background: linear-gradient(160deg, var(--white) 0%, var(--paper) 55%, var(--paper-shade) 100%);
    overflow: hidden;
  }
  .cover-shape { position: absolute; inset: 0; width: 100%; height: 100%; }
  .frame {
    position: absolute; left: 28px; right: 28px; top: 28px; bottom: 28px;
    border: 2px solid var(--teal-line);
  }

  /* Back cover */
  .back-brand {
    position: absolute; left: 0; right: 0;
    display: flex; align-items: center; justify-content: center; gap: 12px;
    font-family: "EB Garamond", serif; font-weight: 600;
    color: var(--teal-deep);
  }
  .back-brand.surgeon { top: 150px; font-size: 26px; }
  .back-brand.institute { top: 250px; font-size: 19px; }
  .brand-circle { width: 34px; height: 34px; border-radius: 50%; background: var(--teal); }
  .brand-square { width: 44px; height: 44px; background: var(--teal-deep); }
  .back-contact {
    position: absolute;
    font-family: "Josefin Sans", sans-serif; font-weight: 600;
    font-size: 12px; line-height: 1.5; color: var(--white);
    white-space: nowrap;
  }
  .address { left: 44px; width: 210px; bottom: 56px; text-align: right; }
  .lines { left: 268px; bottom: 112px; text-align: left; }

  /* Front cover */
  .front-title {
    position: absolute; top: 58px; left: 0; right: 0; text-align: center;
    color: var(--white);
  }
  .front-title .lead {
    font-family: "EB Garamond", serif; font-size: 22px; display: block;
    margin-bottom: 4px; font-weight: 400;
  }
  .front-title .main {
    font-family: "Josefin Sans", sans-serif; font-weight: 700;
    font-size: 54px; line-height: 1; letter-spacing: 1px; display: block;
  }
  .tagline {
    font-family: "EB Garamond", serif; font-style: italic; font-weight: 400;
    font-size: 18px; margin-top: 10px; display: block;
  }
  .front-visual {
    position: absolute; left: 160px; top: 300px; width: 160px; height: 160px;
    border-radius: 50%;
    background: radial-gradient(circle, rgba(22,151,139,.35), rgba(22,151,139,0) 70%);
  }
  .surgeon-plate {
    position: absolute; left: 90px; right: 90px; top: 478px;
    padding: 8px; border-radius: 10px;
    background: rgba(92,186,178,.45);
  }
  .surgeon-plate-inner {
    background: var(--teal-deep); border-radius: 6px;
    border: 1px solid rgba(255,255,255,.5);
    padding: 10px 12px; text-align: center;
    font-family: "EB Garamond", serif; color: var(--white);
  }
  .surgeon-name { font-size: 21px; font-weight: 600; display: block; }
  .surgeon-credentials { font-size: 13px; display: block; line-height: 1.3; }
  .front-brand {
    position: absolute; bottom: 46px; left: 0; right: 0;
    display: flex; align-items: center; justify-content: center; gap: 8px;
    font-family: "EB Garamond", serif; font-weight: 600; font-size: 13px;
    color: var(--teal-deep);
  }
  .front-brand .brand-square { width: 24px; height: 24px; }
</style>
</head>
<body>
<main class="spread">

  <section class="cover back-cover" aria-label="Back cover">
    <svg class="cover-shape" viewBox="0 0 480 680" preserveAspectRatio="none" aria-hidden="true">
      <polygon points="0,525 175,372 480,395 480,680 0,680" fill="var(--lilac-edge)"/>
      <polygon points="0,530 175,380 480,402 480,680 0,680" fill="var(--teal)"/>
    </svg>
    <div class="frame"></div>
    <div class="back-brand surgeon"><span class="brand-circle"></span>Brevin Marsh</div>
    <div class="back-brand institute"><span class="brand-square"></span>Kestrel Institute for Metabolic Surgery</div>
    <p class="back-contact lines">Phone: 03 9412 6083<br>Fax: 03 9417 2865<br>Email: info@kestrelims.com.au</p>
    <p class="back-contact address">Suite 17, Level 3<br>Tallowgate Northern Hospital<br>9 Pemberly Road, Fernwick VIC 3174</p>
  </section>

  <section class="cover front-cover" aria-label="Front cover">
    <svg class="cover-shape" viewBox="0 0 480 680" preserveAspectRatio="none" aria-hidden="true">
      <polygon points="0,0 480,0 480,275 0,430" fill="var(--lilac-edge)"/>
      <polygon points="0,0 480,0 480,266 0,421" fill="var(--teal)"/>
    </svg>
    <div class="frame"></div>
    <h1 class="front-title">
      <span class="lead">Kestrel Institute for</span>
      <span class="main">METABOLIC</span>
      <span class="main">SURGERY</span>
      <span class="tagline">“Experience, Expertise and Empathy”</span>
    </h1>
    <div class="front-visual" role="img" aria-label="Illustration of a curled teal tape measure"></div>
    <div class="surgeon-plate">
      <div class="surgeon-plate-inner">
        <span class="surgeon-name">Mr Brevin Marsh</span>
        <span class="surgeon-credentials">MBBS FRACS GradCert<br>(Health Stats)</span>
      </div>
    </div>
    <div class="front-brand"><span class="brand-square"></span>Kestrel Institute for Metabolic Surgery</div>
  </section>

</main>
</body>
</html>
```